Stationary for mobile ultrasound company
Business card, letter head and envelope design
Stationary for mobile ultrasound company - Imaging
Modern
Lorna Pettibone, RDMS, ARRT
Owner/Operator
5718 N. Quarry Hollow Ln. Halverton, Westmark 83791
lumenscanhealth@corvilmail.net
www. plinthory.com
Please add tag line under logo: Improving ultrasound in a convenient and personal way.
Appointment time and date spaces. Please try logo as is and with black backgrounds on front of card

```html
<!DOCTYPE html>
<html lang="en">
<head>
<meta charset="utf-8">
<title>Lumenscan Health – Business Cards</title>
<link href="https://fonts.googleapis.com/css2?family=Montserrat:wght@400;500;600;800&display=swap" rel="stylesheet">
<style>
  :root {
    --backdrop: #ecebe8;
    --card: #ffffff;
    --purple: #8b3c9f;
    --purple-deep: #6f2a86;
    --teal: #24a39a;
    --ink: #4a4a55;
    --on-purple: #ffffff;
  }
  * { box-sizing: border-box; margin: 0; padding: 0; }
  html, body { width: 1200px; height: 629px; overflow: hidden; }
  body {
    background: var(--backdrop);
    font-family: "Montserrat", Arial, sans-serif;
    position: relative;
  }
  .card {
    position: absolute;
    top: 172px;
    width: 500px;
    height: 286px;
    background: var(--card);
    box-shadow: 0 6px 18px rgba(0,0,0,.12);
    overflow: hidden;
  }
  .card--front { left: 67px; }
  .card--contact { left: 633px; }

  .brand {
    display: flex;
    align-items: center;
    gap: 10px;
    position: absolute;
    left: 50%;
    transform: translateX(-50%);
  }
  .brand__dot {
    width: 26px; height: 26px;
    border-radius: 50%;
    background: var(--teal);
  }
  .brand__name {
    font-weight: 800;
    font-size: 30px;
    letter-spacing: 1px;
    color: var(--purple);
    white-space: nowrap;
  }
  .card--front .brand { top: 112px; }
  .front__web {
    position: absolute;
    bottom: 22px; left: 0; right: 0;
    text-align: center;
    font-size: 11px;
    letter-spacing: 2px;
    color: var(--ink);
  }

  .card--contact .brand { top: 36px; }
  .contact__rule {
    position: absolute;
    top: 113px; left: 0; right: 0;
    height: 3px;
    background: var(--teal);
  }
  .contact__band {
    position: absolute;
    top: 116px; left: 0; right: 0; bottom: 0;
    background: linear-gradient(180deg, var(--purple), var(--purple-deep));
    color: var(--on-purple);
  }
  .person {
    position: absolute;
    left: 26px; top: 62px;
  }
  .person__name { font-size: 12px; font-weight: 600; }
  .person__role { font-size: 10px; margin-top: 3px; }
  .person__address { font-size: 10px; margin-top: 18px; line-height: 1.5; }
  .contact-list {
    position: absolute;
    right: 24px; top: 22px;
    list-style: none;
    font-size: 10px;
  }
  .contact-list li {
    display: flex; align-items: center; gap: 7px;
    height: 21px;
    white-space: nowrap;
  }
  .contact-list svg { width: 13px; height: 13px; flex: none; }
</style>
</head>
<body>
  <section class="card card--front">
    <div class="brand">
      <span class="brand__dot"></span>
      <span class="brand__name">LUMENSCAN</span>
    </div>
    <p class="front__web">www. plinthory.com</p>
  </section>

  <section class="card card--contact">
    <div class="brand">
      <span class="brand__dot"></span>
      <span class="brand__name">LUMENSCAN</span>
    </div>
    <div class="contact__rule"></div>
    <div class="contact__band">
      <div class="person">
        <p class="person__name">Lorna Pettibone, RDMS, ARRT</p>
        <p class="person__role">Owner/Operator</p>
        <p class="person__address">5718 N. Quarry Hollow Ln.<br>Halverton, Westmark 83791</p>
      </div>
      <ul class="contact-list">
        <li>
          <svg viewBox="0 0 14 14"><circle cx="7" cy="7" r="7" fill="#fff"/><path d="M4.5 3.5l1.5 0 .6 2-1 .7a5 5 0 0 0 2.2 2.2l.7-1 2 .6v1.5c-3.5.4-6.4-2.5-6-6z" fill="#8b3c9f"/></svg>
          (208) 555-0142
        </li>
        <li>
          <svg viewBox="0 0 14 14"><circle cx="7" cy="7" r="7" fill="#fff"/><rect x="4" y="5" width="6" height="4.5" fill="#8b3c9f"/><rect x="5" y="3.5" width="4" height="2" fill="#8b3c9f"/></svg>
          (208) 555-0187
        </li>
        <li>
          <svg viewBox="0 0 14 14"><circle cx="7" cy="7" r="7" fill="#fff"/><rect x="5" y="3" width="4" height="8" rx="1" fill="#8b3c9f"/></svg>
          (208) 555-0163
        </li>
        <li>
          <svg viewBox="0 0 14 14"><circle cx="7" cy="7" r="7" fill="#fff"/><rect x="3.5" y="4.5" width="7" height="5" fill="#8b3c9f"/><path d="M3.5 4.5l3.5 3 3.5-3" stroke="#fff" stroke-width=".8" fill="none"/></svg>
          lumenscanhealth@corvilmail.net
        </li>
        <li>
          <svg viewBox="0 0 14 14"><circle cx="7" cy="7" r="7" fill="#fff"/><circle cx="7" cy="7" r="3.5" fill="none" stroke="#8b3c9f" stroke-width="1"/><path d="M3.5 7h7M7 3.5v7" stroke="#8b3c9f" stroke-width=".8"/></svg>
          www. plinthory.com
        </li>
      </ul>
    </div>
  </section>
</body>
</html>
```